Landing Page für Freelancer im Bereich der Informationstechnik
Zielgruppe
Ich bin Experte für Informationstechnik, Unified Communications, Beratung, Management sowie Projekte aller Art.
Mit meiner WOLKENTOR GmbH bin ich als (einzelner) Freelancer für mittelständische Unternehmen und Konzerne in verschiedensten Projekten tätig.
Mein Motto lautet 'Mit Präzision und langjähriger Erfahrung immer alles im Griff!'
Aufgabenstellung
Die aktuell existierende Internet-Präsenz unter wolkentor-web.de beinhaltet aktuell nur eine minimalistische statische Seite sowie das Impressum, ohne jegliche dynamische Inhalte.
DABEI SOLL ES BLEIBEN. Auch die Inhalte sollen unverändert übernommen werden.
Lediglich soll jetzt eine Anlehnung an das zwischenzeitlich vorhandene Logo vorgenommen werden, welches ich mitliefere.
Es geht mir insgesamt nur darum, ein professionelleres Auftreten zu haben, WENN sich denn mal jemand auf die Seite verirrt.
Das Aussehen soll daher modern und dynamisch sein.
ZUSAMMENFASSUNG: Inhalte bleiben 1:1, grafische Anpassung an Logo gewünscht.
Technisch: Statisch, kein Content-Management. Lohnt sich hier nicht.
SEHR WICHTIG: Ich möchte gerne, dass die Lieferung bereits als HTML (und NICHT NUR ALS GRAFIK) erfolgt, ggf. stelle ich auch kurz den FTP-Zugang.
Insgesamt möchte ich gar keine große Sache draus machen.
Viele Anpassungsrunden wird es voraussichtlich nicht geben.
Zeitlich ist dies hier ein sehr kleines Projekt - Erweiterungen kommen später.

```html
<!DOCTYPE html>
<html lang="de">
<head>
<meta charset="utf-8">
<title>WOLKENTOR GmbH – Malte Florian Brandt</title>
<link rel="stylesheet" href="https://fonts.googleapis.com/css2?family=Mulish:wght@500;600;700;800&display=swap">
<style>
  :root {
    --teal: #4aa9c2;
    --teal-line: #a9d3de;
    --ink: #3f3f44;
    --ink-soft: #4a4a50;
    --rule: #cfd2d6;
    --paper: #ffffff;
    --hero-top: #dcdde8;
    --hero-mid: #c9cbdc;
    --hero-low: #eeeff4;
  }
  * { margin: 0; padding: 0; box-sizing: border-box; }
  html, body {
    width: 1200px;
    height: 2596px;
    overflow: hidden;
    background: var(--paper);
    font-family: "Mulish", Arial, sans-serif;
    color: var(--ink);
  }
  .page { position: relative; width: 1200px; height: 2596px; }

  .hero {
    position: absolute; left: 0; top: 0; width: 1200px; height: 575px;
    background: linear-gradient(180deg, var(--hero-top) 0%, var(--hero-mid) 45%, var(--hero-low) 100%);
  }
  .hero-veil {
    position: absolute; left: 98px; top: 350px; width: 1004px; height: 225px;
    background: rgba(255,255,255,0.82);
  }

  .brand {
    position: absolute; left: 0; top: 560px; width: 1200px;
    display: flex; justify-content: center; align-items: center; gap: 22px;
  }
  .brand-dot { width: 40px; height: 40px; border-radius: 50%; background: var(--teal); }
  .brand-name {
    font-size: 44px; font-weight: 700; letter-spacing: 6px; color: var(--ink-soft);
  }

  .motto {
    position: absolute; left: 0; top: 782px; width: 1200px;
    text-align: center; font-size: 39px; font-weight: 700; line-height: 58px;
    text-transform: uppercase; color: var(--ink-soft);
  }

  .rule {
    position: absolute; left: 98px; width: 1004px; height: 2px; background: var(--rule);
  }
  .rule.top { top: 1039px; }
  .rule.bottom { top: 2102px; background: var(--teal-line); }

  .degree {
    position: absolute; left: 98px; top: 1168px;
    font-size: 36px; font-weight: 700; color: var(--ink-soft);
  }
  .person {
    position: absolute; left: 96px; top: 1250px;
    font-size: 78px; font-weight: 600; color: var(--teal); letter-spacing: 0.5px;
  }
  .master {
    position: absolute; left: 98px; top: 1374px;
    font-size: 36px; font-weight: 700; color: var(--ink-soft);
  }

  .mail {
    position: absolute; left: 98px; top: 1590px;
    font-size: 27px; font-weight: 700; color: var(--ink-soft);
    padding-bottom: 8px; border-bottom: 3px solid var(--teal-line);
  }

  .expertise {
    position: absolute; left: 96px; top: 1662px;
    font-size: 56px; font-weight: 700; line-height: 72px; color: var(--ink-soft);
  }
  .invite {
    position: absolute; left: 98px; top: 1910px; width: 1000px;
    font-size: 26px; font-weight: 700; line-height: 41px; color: var(--ink-soft);
  }

  .footer-nav {
    position: absolute; left: 98px; top: 2168px;
    display: flex; gap: 0;
  }
  .footer-nav a {
    font-size: 30px; font-weight: 700; color: var(--ink-soft); text-decoration: none;
  }
  .footer-nav a:nth-child(1) { width: 242px; }
  .footer-nav a:nth-child(2) { width: 257px; }
</style>
</head>
<body>
<main class="page">
  <div class="hero" role="img" aria-label="Draufsicht auf einen Arbeitsplatz mit Laptops, Notizzetteln und Kaffeetasse"></div>
  <div class="hero-veil"></div>

  <div class="brand">
    <span class="brand-dot"></span>
    <span class="brand-name">WOLKENTOR GmbH</span>
  </div>

  <p class="motto">"Mit Präzision und<br>langjähriger Erfahrung immer<br>alles im Griff!"</p>

  <div class="rule top"></div>

  <p class="degree">Diplom-Informatiker (FH)</p>
  <h1 class="person">Malte Florian Brandt</h1>
  <p class="master">Master of Science in Electronic Business</p>

  <p class="mail">m punkt brandt at wolkentor punkt de</p>

  <h2 class="expertise">Experte für Informationstechnik |<br>Unified Communications | Beratung |<br>Management | Projekte aller Art</h2>

  <p class="invite">Gerne schicke ich Ihnen unverbindlich mein Expertenprofil samt CV sowie meine aktuellen Verfügbarkeiten zu. Kontaktieren Sie mich hierzu einfach per E-Mail unter m punkt brandt at wolkentor punkt de. Ich freue mich auf Sie!</p>

  <div class="rule bottom"></div>

  <nav class="footer-nav">
    <a href="#">Startseite</a>
    <a href="#">Impressum</a>
    <a href="#">Datenschutz</a>
  </nav>
</main>
</body>
</html>
```